I'm a magician . hypnotist also a good barber. I need this all to be shown in good detail on the cards.

Magician

Magician/ hypnotist/barber Morris quill. One of the best. Tel 07412 638204
Email.Velvetowl27@postmail-example.net
Title of card velvet owl.

```html
<!DOCTYPE html>
<html lang="en">
<head>
<meta charset="utf-8">
<title>Velvet Owl – Morris Quill</title>
<link rel="stylesheet" href="https://fonts.googleapis.com/css2?family=Cinzel:wght@400;500;700&family=Source+Sans+3:wght@400&display=swap">
<style>
  :root {
    --wine: #8b1c1c;
    --wine-dark: #560a0a;
    --wine-light: #b33434;
    --emblem-dark: #4a0c0c;
    --emblem-mid: #7a1e1e;
    --paper: #ffffff;
    --ink-light: #ffffff;
  }
  * { margin: 0; padding: 0; box-sizing: border-box; }
  html, body { width: 1200px; height: 773px; overflow: hidden; background: var(--paper); }
  .card { position: relative; width: 1200px; height: 773px; background: var(--paper); }

  .brand-title {
    position: absolute; top: 40px; left: 0; width: 100%;
    text-align: center;
    font-family: "Cinzel", serif; font-weight: 500;
    font-size: 110px; line-height: 1; letter-spacing: 1px;
    color: var(--wine);
  }

  .emblem {
    position: absolute; left: 504px; top: 154px; width: 192px; height: 200px;
    border-radius: 50% 50% 46% 46% / 40% 40% 14% 14%;
    background: radial-gradient(ellipse at 50% 40%, var(--emblem-mid), var(--emblem-dark));
  }

  .divider-line {
    position: absolute; left: 14px; right: 8px; top: 373px; height: 7px;
    background: var(--wine-dark);
  }

  .contact-band {
    position: absolute; left: 14px; right: 0; top: 389px; bottom: 0;
    background: radial-gradient(ellipse 55% 75% at 50% 62%, var(--wine-light), var(--wine) 45%, var(--wine-dark) 100%);
    color: var(--ink-light);
    text-align: center;
  }

  .person-name {
    position: absolute; top: 50px; left: 0; width: 100%;
    font-family: "Cinzel", serif; font-weight: 500;
    font-size: 55px; line-height: 1; letter-spacing: 1px;
  }

  .services {
    position: absolute; top: 134px; left: 0; width: 100%;
    font-family: "Source Sans 3", sans-serif;
    font-size: 33px; letter-spacing: 1.5px; text-transform: uppercase;
  }
  .services .sep { margin: 0 10px; }

  .phone, .email {
    position: absolute; left: 0; width: 100%;
    display: flex; justify-content: center; align-items: center; gap: 10px;
  }
  .phone {
    top: 214px;
    font-family: "Cinzel", serif; font-weight: 700;
    font-size: 37px; letter-spacing: 1px;
  }
  .email {
    top: 297px;
    font-family: "Source Sans 3", sans-serif;
    font-size: 33px;
  }
  .icon { fill: none; stroke: var(--ink-light); }
</style>
</head>
<body>
<main class="card">
  <h1 class="brand-title">VELVET OWL</h1>

  <div class="emblem" role="img" aria-label="Brand emblem area"></div>

  <div class="divider-line"></div>

  <section class="contact-band">
    <h2 class="person-name">MORRIS QUILL</h2>
    <p class="services">Magician<span class="sep">|</span>Hypnotist<span class="sep">|</span>Barber</p>
    <p class="phone">
      <svg class="icon" width="22" height="36" viewBox="0 0 22 36" aria-hidden="true">
        <rect x="2" y="2" width="18" height="32" rx="4" fill="#fff" stroke="none"/>
        <rect x="5" y="6" width="12" height="10" rx="1" fill="#8b1c1c" stroke="none"/>
      </svg>
      07412 638204
    </p>
    <p class="email">
      <svg class="icon" width="40" height="26" viewBox="0 0 40 26" aria-hidden="true">
        <rect x="2" y="2" width="36" height="22" stroke-width="3"/>
        <path d="M2 2 L20 15 L38 2" stroke-width="3"/>
      </svg>
      velvetowl27@postmail-example.net
    </p>
  </section>
</main>
</body>
</html>
```